KV Taxidermy

I need business Cards with my logo and a background photo of one of my taxidermy mounts.
I would like a black back drop behind it all and what ever looks best for my contact information (red or white?)
Marcus Pellow
555-218-4907
kvtaxidermy512@mailvex.net
Chatterly page

```html
<!DOCTYPE html>
<html lang="en">
<head>
<meta charset="utf-8">
<title>KV Taxidermy – Business Card</title>
<link rel="stylesheet" href="https://fonts.googleapis.com/css2?family=Oswald:wght@500;600&family=Lato:wght@400&display=swap">
<style>
  :root {
    --page-bg: #e9e7e4;
    --card-black: #000000;
    --text-white: #ffffff;
    --disc-light: #f4f3f2;
    --disc-mid: #dcdad8;
    --mark-ink: #111111;
  }
  html, body {
    margin: 0;
    padding: 0;
    width: 1200px;
    height: 900px;
    overflow: hidden;
    background: var(--page-bg);
  }
  .business-card {
    position: absolute;
    left: 120px;
    top: 154px;
    width: 960px;
    height: 592px;
    background: var(--card-black);
    color: var(--text-white);
    overflow: hidden;
  }
  .holder-name {
    position: absolute;
    left: 57px;
    top: 86px;
    margin: 0;
    font-family: "Oswald", "Arial Narrow", sans-serif;
    font-weight: 600;
    font-size: 34px;
    letter-spacing: 0.2px;
    line-height: 1;
    text-transform: uppercase;
  }
  .contact-line {
    position: absolute;
    left: 57px;
    display: flex;
    align-items: center;
    gap: 12px;
    font-family: "Lato", "Helvetica", sans-serif;
    font-size: 25px;
    line-height: 1;
    white-space: nowrap;
  }
  .contact-line svg { flex: none; }
  .contact-social { top: 361px; }
  .contact-phone { top: 446px; }
  .contact-email { top: 481px; }
  .social-dot {
    width: 26px;
    height: 26px;
    border-radius: 50%;
    background: var(--text-white);
    flex: none;
  }
  .brand-disc {
    position: absolute;
    left: 397px;
    top: 38px;
    width: 512px;
    height: 512px;
    border-radius: 50%;
    background: radial-gradient(circle at 50% 45%, var(--disc-light) 0%, var(--disc-mid) 100%);
    display: flex;
    align-items: center;
    justify-content: center;
  }
  .brand-name {
    font-family: "Oswald", "Arial Narrow", sans-serif;
    font-weight: 600;
    font-size: 54px;
    letter-spacing: 4px;
    color: var(--mark-ink);
    text-transform: uppercase;
  }
</style>
</head>
<body>
  <div class="business-card">
    <h1 class="holder-name">Marcus Pellow</h1>

    <div class="contact-line contact-social">
      <span class="social-dot"></span>
      <span>chatterly@kvtaxidermy</span>
    </div>

    <div class="contact-line contact-phone">
      <svg width="22" height="20" viewBox="0 0 22 20" aria-hidden="true">
        <path d="M2 7c0-3 4-5 9-5s9 2 9 5v2h-5V7c-2-1-6-1-8 0v2H2z" fill="#fff"/>
        <path d="M6 10h10l3 8H3z" fill="#fff"/>
        <circle cx="11" cy="14" r="2" fill="#000"/>
      </svg>
      <span>555-218-4907</span>
    </div>

    <div class="contact-line contact-email">
      <svg width="22" height="16" viewBox="0 0 22 16" aria-hidden="true">
        <rect x="0" y="0" width="22" height="16" fill="#fff"/>
        <path d="M1 1l10 8 10-8" fill="none" stroke="#000" stroke-width="1.6"/>
      </svg>
      <span>kvtaxidermy512@mailvex.net</span>
    </div>

    <div class="brand-disc">
      <span class="brand-name">KV Taxidermy</span>
    </div>
  </div>
</body>
</html>
```